Brightfield Sunray Panel cleaning business needs a flyer designed.

I need a flyer design for a new company based in Los Angeles. We clean solar panels at an affordable price, we're insured, and licensed. we would like the design to include the colors Red, white, and Blue. The flyer should emphasize the importance of cleaning solar panels to maintain the warranty and add longevity to the solar panels.

```html
<!DOCTYPE html>
<html lang="en">
<head>
<meta charset="utf-8">
<title>Brightfield Sunray Panel Cleaning Flyer</title>
<link href="https://fonts.googleapis.com/css2?family=Montserrat:wght@500;700;800&family=Saira+Condensed:wght@700&family=Open+Sans:wght@600&display=swap" rel="stylesheet">
<style>
  :root {
    --red: #be1a20;
    --red-deep: #b3161c;
    --blue: #2d3589;
    --white: #ffffff;
    --sky: #2a8fc0;
    --panel: #1d3550;
  }
  html, body { margin: 0; padding: 0; overflow: hidden; }
  body { width: 960px; height: 1200px; background: var(--red); font-family: "Montserrat", sans-serif; color: var(--white); }
  .flyer { position: relative; width: 960px; height: 1200px; overflow: hidden; background: var(--red); }

  .brand { position: absolute; left: 0; top: 0; width: 960px; height: 255px; background: var(--red); }
  .brand-top { position: absolute; left: 0; top: 0; width: 960px; height: 47px; background: var(--red-deep); }
  .brand-name { position: absolute; left: 0; top: 78px; width: 960px; text-align: center; font-weight: 800; font-size: 64px; letter-spacing: 2px; line-height: 1; }
  .brand-tagline { position: absolute; left: 40px; top: 168px; width: 800px; height: 22px; background: var(--blue); clip-path: polygon(8px 0, 100% 0, calc(100% - 8px) 100%, 0 100%); font-weight: 800; font-size: 15px; letter-spacing: 19px; text-align: center; line-height: 22px; }

  .stripe-blue { position: absolute; left: 0; top: 255px; width: 960px; height: 22px; background: var(--blue); }
  .stripe-red { position: absolute; left: 0; top: 277px; width: 960px; height: 21px; background: var(--red); }

  .hero { position: absolute; left: 0; top: 298px; width: 960px; height: 304px; background: var(--blue); }
  .headline { position: absolute; left: 0; top: 32px; width: 960px; margin: 0; text-align: center; font-family: "Saira Condensed", sans-serif; font-weight: 700; font-size: 58px; line-height: 74px; letter-spacing: 2px; }
  .pills { position: absolute; left: 41px; top: 199px; display: flex; gap: 21px; }
  .pill { width: 280px; height: 63px; border-radius: 16px; background: var(--red); font-weight: 800; font-size: 33px; line-height: 63px; text-align: center; letter-spacing: 0.5px; }

  .benefits { position: absolute; left: 0; top: 602px; width: 960px; height: 492px; background: var(--red); }
  .benefit { position: absolute; left: 41px; width: 440px; }
  .benefit-title { display: inline-block; background: var(--blue); padding: 0 26px 0 8px; height: 22px; line-height: 23px; font-weight: 700; font-size: 16.5px; clip-path: polygon(0 0, calc(100% - 12px) 0, 100% 100%, 0 100%); }
  .benefit-text { margin: 4px 0 0 2px; font-weight: 500; font-size: 14.6px; line-height: 18.4px; }

  .photo-frame { position: absolute; left: 0; top: 0; }

  .contact { position: absolute; left: 0; top: 1094px; width: 960px; height: 106px; background: var(--blue); }
  .contact-box { position: absolute; left: 24px; top: 20px; width: 911px; height: 64px; background: var(--red); font-family: "Open Sans", sans-serif; font-weight: 600; font-size: 24px; }
  .contact-item { position: absolute; top: 0; height: 64px; display: flex; align-items: center; gap: 14px; }
  .contact-phone { left: 32px; }
  .contact-email { left: 345px; }
</style>
</head>
<body>
<div class="flyer">
  <header class="brand">
    <div class="brand-top"></div>
    <div class="brand-name">BRIGHTFIELD SUNRAY</div>
    <div class="brand-tagline">SOLAR PANEL CLEANING</div>
  </header>
  <div class="stripe-blue"></div>
  <div class="stripe-red"></div>

  <section class="hero">
    <h1 class="headline">PROTECT YOUR WARRANTY AND<br>YOUR INVESTMENT</h1>
    <div class="pills">
      <div class="pill">AFORDABLE</div>
      <div class="pill">INSURED</div>
      <div class="pill">LICENSED</div>
    </div>
  </section>

  <section class="benefits">
    <svg class="photo-frame" width="960" height="492" viewBox="0 0 960 492">
      <defs>
        <linearGradient id="panelTone" x1="0" y1="0" x2="1" y2="1">
          <stop offset="0" stop-color="#2f7fae"/>
          <stop offset="0.45" stop-color="var(--panel)"/>
          <stop offset="1" stop-color="#2a6e9c"/>
        </linearGradient>
      </defs>
      <polygon points="558,21 960,21 960,471 384,471" fill="var(--blue)"/>
      <polygon points="573,21 960,21 960,448 414,448" fill="var(--white)"/>
      <polygon role="img" aria-label="Photo of clean solar panels against a blue sky" points="592,21 960,21 960,428 445,428" fill="url(#panelTone)"/>
    </svg>

    <div class="benefit" style="top:53px">
      <div class="benefit-title">MAXIMIZE ENERGY EFFICIENCY</div>
      <p class="benefit-text">Clean solar panels absorb more sunlight,<br>boosting energy output and saving you money<br>on electricity bills.</p>
    </div>
    <div class="benefit" style="top:146px; left:45px">
      <div class="benefit-title">PROTECT YOUR INVESTMENT</div>
      <p class="benefit-text">Regular cleaning helps maintain your solar panel<br>warranty and extends their lifespan.</p>
    </div>
    <div class="benefit" style="top:221px; left:45px">
      <div class="benefit-title">ECO-FRIENDLY POWER</div>
      <p class="benefit-text">Clean panels ensure optimal performance,<br>maximizing your contribution to sustainable<br>energy.</p>
    </div>
    <div class="benefit" style="top:309px; left:47px">
      <div class="benefit-title">AFFORDABLE &amp; RELIABLE SERVICE</div>
      <p class="benefit-text">Professional cleaning at competitive prices,<br>backed by insurance and licensing for peace<br>of mind.</p>
    </div>
    <div class="benefit" style="top:397px; left:48px">
      <div class="benefit-title">ENHANCED AESTHETIC APPEAL</div>
      <p class="benefit-text">Keep your solar panels looking clean and<br>well-maintained, improving the overall<br>appearance of your property.</p>
    </div>
  </section>

  <footer class="contact">
    <div class="contact-box">
      <div class="contact-item contact-phone">
        <svg width="44" height="44" viewBox="0 0 44 44" aria-hidden="true">
          <circle cx="22" cy="22" r="22" fill="var(--white)"/>
          <path d="M15 11c1-1 2.5-1 3.3 0l3 3.8c.7.9.6 2-.2 2.8l-1.8 1.6c1.2 2.6 3 4.4 5.5 5.6l1.7-1.8c.8-.8 2-.9 2.8-.2l3.8 3c1 .8 1 2.3 0 3.3l-1.8 1.8c-1.5 1.5-4 1.8-6.3.6C18.8 29 14.8 25 12.3 19.6c-1.2-2.3-.9-4.8.6-6.3z" fill="var(--red)"/>
        </svg>
        <span>626-555-0142</span>
      </div>
      <div class="contact-item contact-email">
        <svg width="44" height="44" viewBox="0 0 44 44" aria-hidden="true" fill="none" stroke="var(--white)" stroke-width="3">
          <circle cx="22" cy="22" r="19"/>
          <ellipse cx="22" cy="22" rx="8" ry="19"/>
          <line x1="22" y1="3" x2="22" y2="41"/>
          <line x1="3" y1="22" x2="41" y2="22"/>
          <path d="M6 12.5h32M6 31.5h32"/>
        </svg>
        <span>ALEX@BRIGHTFIELDSUNRAY.COM</span>
      </div>
    </div>
  </footer>
</div>
</body>
</html>
```